Biz Card Design TPVC

New business card for a new company.
Logo was completed by a designer on ArtFlock and looking to continue requesting additional services.
Company Name: Tidal Prime Voltage Collective
Although this company is starting in Canada, we will be moving towards a global presence within the next 6 months.
Key elements to this business are as follows.
Energy Procurement
Energy Reduction Services
Demand Side Consulting
Energy Efficiency Consulting
Saving Clients Money
Helping Them Go "Green"
Managing Their Energy Requirements
Basically the goal for our company is to find the best procurement solution for our clients and reduce their energy consumption. This reduces their expenses and the amount of greenhouse gas they produce on a daily basis.
I have been in the energy footprint for the last 20 years and know that most companies are looking to "do whatever is necessary to get them to sign on the dotted line". I would prefer to walk away from a client that I can't help than to put them into a situation that they will regret for years to come. This is where the "TIDAL" part of the company name comes from.
The following is a catch phrase that encompasses what we do.
"Reducing your carbon footprint & energy bill at the same time!"
The back of the card needs to have this statement along with some sort of illustration. The back is a playground for creative ideas.
The front of the card needs the following.
Logo.
First & Last Name (Gus Marwick)
Title (Energy Warrior)
Phone Number (555) 314-2768
Fax Number (555) 862-4091
Email Address gus@tidalprimevoltage.example
Address 47 Orchard Lane Toronto Ontario K4P 2Z7
I want it to be a card that is remembered when any of my staff give it to a customer. It HAS to stand out.
Target Market(s)
Business Owners, Decision Makers, 30 to 65+
Industry/Entity Type
Business
Look and feel
Each slider illustrates characteristics of the customer's brand and the style your logo design should communicate.

```html
<!DOCTYPE html>
<html lang="en">
<head>
<meta charset="utf-8">
<title>Tidal Prime Voltage Collective – Business Card</title>
<link rel="stylesheet" href="https://fonts.googleapis.com/css2?family=Open+Sans:wght@400;600;700;800&family=Exo+2:wght@300;700&display=swap">
<style>
  :root {
    --page-bg: #e9e6e1;
    --green-light: #3da957;
    --green-mid: #2b9245;
    --green-dark: #1d7433;
    --stripe-blue: #2f5fae;
    --stripe-green: #5bbf4a;
    --logo-blue: #2a5cab;
    --white: #ffffff;
    --soft-white: rgba(255,255,255,0.85);
    --photo-warm: #c9a27c;
    --photo-suit: #2b2b2e;
  }
  * { box-sizing: border-box; margin: 0; padding: 0; }
  html, body { width: 1200px; height: 880px; overflow: hidden; }
  body {
    background: var(--page-bg);
    font-family: "Open Sans", Arial, sans-serif;
    position: relative;
  }
  .card {
    position: absolute;
    left: 250px;
    width: 700px;
    height: 400px;
    overflow: hidden;
    border-radius: 4px;
    box-shadow: 0 6px 18px rgba(0,0,0,0.18);
  }
  .card--front { top: 30px; background: linear-gradient(160deg, var(--green-light), var(--green-dark)); }
  .card--back { top: 450px; background: linear-gradient(150deg, var(--green-light) 0%, var(--green-mid) 55%, var(--green-dark) 100%); }

  .front-swoosh { position: absolute; inset: 0; width: 700px; height: 400px; }

  .brand {
    position: absolute;
    top: 86px;
    right: 36px;
    display: flex;
    align-items: center;
    gap: 12px;
  }
  .brand__dot { width: 22px; height: 22px; border-radius: 50%; background: var(--stripe-green); }
  .brand__name {
    font-weight: 800;
    font-size: 27px;
    letter-spacing: -0.5px;
    color: var(--logo-blue);
  }

  .person { position: absolute; left: 62px; top: 198px; color: var(--white); }
  .person__name { font-weight: 700; font-size: 30px; line-height: 1.1; }
  .person__title { font-size: 16px; margin-top: 4px; color: var(--soft-white); }

  .website {
    position: absolute; left: 40px; top: 320px;
    color: var(--white); font-size: 16px;
  }
  .divider {
    position: absolute; left: 378px; top: 262px;
    width: 1px; height: 120px; background: var(--soft-white);
  }
  .contact {
    position: absolute; left: 398px; top: 260px;
    list-style: none; color: var(--white); font-size: 15px; line-height: 22px;
  }
  .contact li { display: flex; align-items: flex-start; gap: 10px; }
  .contact svg { width: 16px; height: 16px; margin-top: 3px; flex: none; fill: var(--white); }
  .contact .indent { padding-left: 26px; }

  .tagline {
    position: absolute; left: 46px; top: 112px;
    font-family: "Exo 2", Arial, sans-serif;
    color: var(--white); font-size: 27px; line-height: 1.32;
  }
  .tagline__light { font-weight: 300; }
  .tagline__bold { font-weight: 700; }

  .back-photo {
    position: absolute; right: 0; top: 0;
    width: 370px; height: 400px;
    background:
      linear-gradient(180deg, rgba(168,138,60,0.55) 0%, rgba(168,138,60,0) 45%),
      linear-gradient(90deg, rgba(43,146,69,0) 0%, var(--photo-warm) 38%, var(--photo-warm) 72%, var(--photo-suit) 92%);
    opacity: 0.9;
  }
</style>
</head>
<body>

<section class="card card--front" aria-label="Business card front">
  <svg class="front-swoosh" viewBox="0 0 700 400" aria-hidden="true">
    <path d="M0 0 H700 V262 C520 240 300 190 0 150 Z" fill="#5bbf4a"/>
    <path d="M0 0 H700 V254 C520 232 300 182 0 142 Z" fill="#2f5fae"/>
    <path d="M0 0 H700 V244 C520 222 300 172 0 132 Z" fill="#ffffff"/>
    <polygon points="0,150 20,160 0,170" fill="#2f5fae"/>
  </svg>

  <div class="brand">
    <span class="brand__dot"></span>
    <span class="brand__name">Tidal Prime Voltage Collective</span>
  </div>

  <div class="person">
    <p class="person__name">Gus Marwick</p>
    <p class="person__title">Energy Warrior</p>
  </div>

  <p class="website">tidalprimevoltage.example</p>
  <span class="divider"></span>

  <ul class="contact">
    <li>
      <svg viewBox="0 0 16 16"><rect x="4" y="1" width="8" height="14" rx="1.5"/><rect x="5.5" y="3" width="5" height="7" fill="#2b9245"/></svg>
      (555) 314-2768
    </li>
    <li>
      <svg viewBox="0 0 16 16"><rect x="4" y="1" width="8" height="5"/><rect x="1" y="6" width="14" height="7" rx="1"/><rect x="4" y="11" width="8" height="4"/></svg>
      (555) 862-4091
    </li>
    <li>
      <svg viewBox="0 0 16 16"><rect x="1" y="3" width="14" height="10" rx="1"/><path d="M1.5 3.5 L8 9 L14.5 3.5" stroke="#2b9245" stroke-width="1.4" fill="none"/></svg>
      gus@tidalprimevoltage.example
    </li>
    <li>
      <svg viewBox="0 0 16 16"><path d="M8 1 L15 8 H13 V15 H9.5 V10.5 H6.5 V15 H3 V8 H1 Z"/></svg>
      47 Orchard Lane Toronto
    </li>
    <li class="indent">Ontario K4P 2Z7</li>
  </ul>
</section>

<section class="card card--back" aria-label="Business card back">
  <div class="back-photo" role="img" aria-label="Photo of cupped hands holding coins with a young plant sprouting from them"></div>
  <p class="tagline">
    <span class="tagline__light">Reducing your</span><br>
    <span class="tagline__bold">carbon footprint &amp;</span><br>
    <span class="tagline__bold">energy bill</span><br>
    <span class="tagline__light">at the same time!</span>
  </p>
</section>

</body>
</html>
```